High End Business Card Design for Flooring Store

Looking for a new card design for our hardwood flooring company. We have no print budget for these and are open to cards made from wood, metal, cardstock with embossed print ... or any combination of these. No plastic.

We sell luxury products and I want the cards to reflect our image of quality and class.

Our contact information as such;
Employee Name
418 Colbrook Blvd.
Dieppe, NB
K9R-3M5
(555) 214-3968
Employee email @velkaflooring.com

Target Market(s)

Home Builders

Contact Information for Business Card

Emnployee name, business contact information

```html
<!DOCTYPE html>
<html lang="en">
<head>
<meta charset="utf-8">
<title>Velka Flooring – Business Card</title>
<link rel="stylesheet" href="https://fonts.googleapis.com/css2?family=Lato:wght@400;700&family=Montserrat:wght@500;700&display=swap">
<style>
  :root {
    --page: #2b2c2f;
    --card: #232326;
    --red: #a5282a;
    --gold: #f0b323;
    --white: #f2f2f2;
    --grey: #b9b9bc;
    --rule: #4a4a4e;
  }
  * { box-sizing: border-box; margin: 0; padding: 0; }
  html, body { width: 1200px; height: 952px; overflow: hidden; }
  body {
    background: var(--page);
    font-family: "Lato", sans-serif;
    position: relative;
  }
  .card {
    position: absolute;
    width: 540px;
    height: 310px;
    background: var(--card);
    box-shadow: 0 14px 30px rgba(0,0,0,.45);
    overflow: hidden;
  }
  .card--front { left: 330px; top: 140px; }
  .card--back  { left: 330px; top: 500px; }

  .wordmark {
    font-family: "Lato", sans-serif;
    font-weight: 400;
    color: var(--red);
    line-height: 1;
    letter-spacing: 1px;
  }
  .tagline {
    color: var(--grey);
    font-size: 15px;
    line-height: 1.2;
  }

  /* front */
  .front-brand {
    position: absolute;
    left: 50%; top: 50%;
    transform: translate(-50%, -50%);
    text-align: left;
  }
  .front-brand .wordmark { font-size: 84px; }
  .front-brand .tagline { margin-top: 6px; padding-left: 8px; font-size: 18px; }

  /* back */
  .accent {
    position: absolute;
    width: 10px;
    background: var(--red);
  }
  .accent--top { left: 0; top: 0; height: 96px; }
  .accent--bottom { right: 0; bottom: 0; height: 110px; }

  .back-brand { position: absolute; left: 50px; top: 72px; }
  .back-brand .wordmark { font-size: 52px; }
  .back-brand .tagline { margin-top: 4px; padding-left: 6px; font-size: 12px; }

  .divider {
    position: absolute;
    left: 262px; top: 56px;
    width: 1px; height: 150px;
    background: var(--rule);
  }

  .contact { position: absolute; left: 290px; top: 64px; }
  .name {
    font-family: "Montserrat", sans-serif;
    font-weight: 500;
    color: var(--gold);
    font-size: 17px;
    letter-spacing: .5px;
    text-transform: uppercase;
  }
  .name strong { font-weight: 700; }
  .role { color: var(--white); font-size: 13px; margin: 2px 0 14px; }
  .contact-list { list-style: none; }
  .contact-list li {
    display: flex; align-items: center; gap: 8px;
    color: var(--white); font-size: 13px; margin-bottom: 6px;
  }
  .contact-list svg { width: 12px; height: 12px; fill: var(--gold); flex: none; }

  .address {
    position: absolute;
    left: 50px; bottom: 40px;
    color: var(--white);
    font-size: 12.5px;
  }
</style>
</head>
<body>

<section class="card card--front" aria-label="Card front">
  <div class="front-brand">
    <div class="wordmark">Velka</div>
    <div class="tagline">Planchers &amp; Escaliers<br>Flooring &amp; Stairs</div>
  </div>
</section>

<section class="card card--back" aria-label="Card back">
  <span class="accent accent--top"></span>
  <span class="accent accent--bottom"></span>

  <div class="back-brand">
    <div class="wordmark">Velka</div>
    <div class="tagline">Planchers &amp; Escaliers<br>Flooring &amp; Stairs</div>
  </div>

  <span class="divider"></span>

  <div class="contact">
    <div class="name">Marcel D. <strong>Arsenault</strong></div>
    <div class="role">Managing Director</div>
    <ul class="contact-list">
      <li>
        <svg viewBox="0 0 24 24" aria-hidden="true"><path d="M6.6 10.8a15 15 0 0 0 6.6 6.6l2.2-2.2c.3-.3.7-.4 1-.2 1.1.4 2.3.6 3.6.6.6 0 1 .4 1 1V20c0 .6-.4 1-1 1A17 17 0 0 1 3 4c0-.6.4-1 1-1h3.5c.6 0 1 .4 1 1 0 1.3.2 2.5.6 3.6.1.3 0 .7-.2 1z"/></svg>
        (555) 214-3968
      </li>
      <li>
        <svg viewBox="0 0 24 24" aria-hidden="true"><path d="M2 5h20v14H2z M2 5l10 8 10-8" fill="var(--gold)"/><path d="M3 6l9 7 9-7" fill="none" stroke="#232326" stroke-width="2"/></svg>
        marcel@velkaflooring.com
      </li>
      <li>
        <svg viewBox="0 0 24 24" aria-hidden="true"><circle cx="12" cy="12" r="10"/><path d="M2 12h20M12 2c3 3 3 17 0 20M12 2c-3 3-3 17 0 20" fill="none" stroke="#232326" stroke-width="1.5"/></svg>
        www.velkaflooring.com
      </li>
    </ul>
  </div>

  <div class="address">418 Colbrook Blvd. Dieppe, NB K9R-3M5</div>
</section>

</body>
</html>
```